Holtvane.co.uk Double Sided A4 Folder needs designing
Holtvane.co.uk needs a folder design
• June 11, 2011 6:13 PM holtvane
Hi
Thanks you so much for the great designs, we prefer more blue than gold, some of the designs have way to much gold..
Derek
• June 10, 2011 7:43 AM RuvenKolt
Thank you so much Dravik ...
• June 10, 2011 7:17 AM Dravik
nice work @ RuvenKolt :)
• June 10, 2011 3:48 AM RuvenKolt
@Project Holder.
Need your feedback please.
Thanks
RuvenKolt
• June 8, 2011 6:33 AM holtvane
We deal with properties in the mayfair area, you can view the mayfair website to get an idea of the area.
http://www.brindlecourt-guide.co.uk/
The title could be 'Your Mayfair Estate Agents'
the look of the folder should have our color blue and gold, ie royal blue and gold design, it should look almost like it is a royal invitation..
examples of some ideas of the design you can get some inspiration below
http://www.printquell.co.uk/royal_blue_and_gold_monogram_wedding_invitation-550218734910267341
http://www.snapvessel.com/photos/inkharbor/5038261947/
http://img.quellcdn.com/royal_blue_and_gold_floral_envelope_fits_5x7_sizes-p48210937755102846613eg6_325.jpg?t_image1_iid=AB3D1185-2276-4F1C-B903-771DE4AC02FA&t_text1=Marla%20Quint%0D%0A518%20Thistleby%20Lane%0D%0ACorrow%20Falls%2C%20NY%2098765
Our address is as below
Holt Vane
14b Pellgrave Row
Mayfair
London
W9X 4QP
• June 8, 2011 2:35 AM QTRVELOSO
Dear PH,
Don't you think, an address or any contact info/tagline would be appropriate to be placed on the folder.
Could you give more details on your business (what kind of properties do you deal with/ May be necessary in case of use of images

```html
<!DOCTYPE html>
<html lang="en">
<head>
<meta charset="utf-8">
<title>Holt Vane – Folder Design</title>
<link rel="stylesheet" href="https://fonts.googleapis.com/css2?family=Jost:wght@500;600&family=Cinzel:wght@500&family=Open+Sans:wght@400&display=swap">
<style>
  :root{
    --stage:#2b2b2d;
    --navy:#0b3a86;
    --royal:#1a4a99;
    --azure:#0a6cc0;
    --sky:#1596df;
    --gold:#e8b51c;
    --gold-deep:#b98326;
    --gold-pale:#e6c79a;
    --yellow:#f8d210;
    --yellow-deep:#dcae2a;
    --paper:#ffffff;
    --paper-shade:#eceef0;
    --label:#ffffff;
  }
  *{box-sizing:border-box;margin:0;padding:0}
  html,body{width:1200px;height:1156px;overflow:hidden}
  body{background:var(--stage);position:relative;font-family:"Open Sans",sans-serif}

  .sheet-label{position:absolute;color:var(--label);font-size:24px;text-decoration:underline;text-underline-offset:5px;text-decoration-thickness:1px}
  .sheet-label--cover{left:60px;top:18px}
  .sheet-label--inner-1{left:60px;top:596px}
  .sheet-label--inner-2{left:620px;top:596px}

  /* Cover spread */
  .cover{position:absolute;left:60px;top:64px;width:1080px;height:500px;overflow:hidden;box-shadow:0 6px 20px rgba(0,0,0,.5)}
  .cover__back{position:absolute;left:0;top:0;width:540px;height:500px;
    background:linear-gradient(160deg,var(--navy) 30%,var(--azure) 100%)}
  .cover__stripe{position:absolute;top:0;bottom:0}
  .cover__stripe--a{left:0;width:38px;background:var(--royal)}
  .cover__stripe--b{left:38px;width:28px;background:#0d3f8e}
  .cover__stripe--c{left:66px;width:20px;background:#174a9c}
  .cover__brand{position:absolute;left:0;width:540px;top:380px;text-align:center;color:var(--paper)}
  .brand-mark{display:inline-block;width:44px;height:44px;border-radius:50%;border:3px solid currentColor}
  .brand-name{display:block;font-family:"Cinzel",serif;font-weight:500;letter-spacing:.28em;font-size:13px;margin-top:8px;white-space:nowrap}
  .cover__address{font-size:8px;line-height:1.3;margin-top:3px}

  .cover__front{position:absolute;left:540px;top:0;width:540px;height:500px;background:var(--paper)}
  .cover__map{position:absolute;left:0;top:0;width:540px;height:500px;
    background:linear-gradient(175deg,var(--sky) 0%,var(--azure) 45%,var(--navy) 100%)}
  .cover__curve{position:absolute;left:0;top:0}
  .cover__title{position:absolute;left:60px;top:290px;font-family:"Jost",sans-serif;font-weight:600;line-height:.9;white-space:nowrap}
  .cover__title-your{display:block;color:var(--paper);font-size:20px}
  .cover__title-place{display:block;color:var(--gold);font-size:60px;letter-spacing:-.01em}
  .cover__title-trade{display:block;color:var(--paper);font-size:21px;margin-left:60px;margin-top:2px}
  .cover__logo{position:absolute;right:8px;top:355px;width:134px;text-align:center;color:var(--navy)}
  .cover__logo .brand-mark{width:50px;height:50px}

  /* Inner spreads */
  .inner{position:absolute;top:640px;width:520px;height:368px;box-shadow:0 6px 20px rgba(0,0,0,.5);
    background:linear-gradient(180deg,var(--paper) 0%,var(--paper-shade) 100%)}
  .inner--blue{left:60px}
  .inner--gold{left:620px}
  .inner svg{display:block}
</style>
</head>
<body>

<span class="sheet-label sheet-label--cover">Cover</span>

<section class="cover" aria-label="Folder cover spread">
  <div class="cover__back">
    <span class="cover__stripe cover__stripe--a"></span>
    <span class="cover__stripe cover__stripe--b"></span>
    <span class="cover__stripe cover__stripe--c"></span>
    <div class="cover__brand">
      <span class="brand-mark"></span>
      <span class="brand-name">HOLT VANE</span>
      <p class="cover__address">14b Pellgrave Row<br>Mayfair, London W9X 4QP</p>
    </div>
  </div>

  <div class="cover__front">
    <div class="cover__map" role="img" aria-label="Faint street map of Mayfair and the West End in blue tones"></div>
    <svg class="cover__curve" width="540" height="500" viewBox="0 0 540 500" aria-hidden="true">
      <defs>
        <linearGradient id="goldLine" x1="0" y1="0" x2="0" y2="1">
          <stop offset="0" stop-color="var(--gold-deep)"/>
          <stop offset=".5" stop-color="var(--gold-pale)"/>
          <stop offset="1" stop-color="var(--gold-deep)"/>
        </linearGradient>
      </defs>
      <path d="M440 0 C540 150 460 380 270 500 L540 500 L540 0 Z" fill="var(--paper)"/>
      <g fill="none" stroke="url(#goldLine)">
        <path d="M440 0 C540 150 460 380 270 500" stroke-width="3"/>
        <path d="M449 0 C549 150 469 380 281 500" stroke-width="2"/>
        <path d="M458 0 C558 150 478 380 292 500" stroke-width="3"/>
        <path d="M467 0 C567 150 487 380 303 500" stroke-width="2"/>
        <path d="M477 0 C577 150 497 380 316 500" stroke-width="1.5"/>
      </g>
    </svg>
    <h1 class="cover__title">
      <span class="cover__title-your">YOUR</span>
      <span class="cover__title-place">MAYFAIR</span>
      <span class="cover__title-trade">ESTATE AGENTS</span>
    </h1>
    <div class="cover__logo">
      <span class="brand-mark"></span>
      <span class="brand-name">HOLT VANE</span>
    </div>
  </div>
</section>

<span class="sheet-label sheet-label--inner-1">Inner Option 01</span>
<section class="inner inner--blue" aria-label="Inner spread, blue pockets">
  <svg width="520" height="368" viewBox="0 0 520 368" aria-hidden="true">
    <defs>
      <linearGradient id="pocketBlue" x1="0" y1="0" x2="1" y2="0">
        <stop offset="0" stop-color="var(--royal)"/>
        <stop offset=".6" stop-color="var(--azure)"/>
        <stop offset="1" stop-color="var(--royal)"/>
      </linearGradient>
    </defs>
    <line x1="260" y1="0" x2="260" y2="368" stroke="#c9cbce"/>
    <polygon points="0,190 240,190 258,368 0,368" fill="url(#pocketBlue)"/>
    <polygon points="280,190 520,190 520,368 262,368" fill="url(#pocketBlue)"/>
    <g stroke="var(--paper)" stroke-width="1.2">
      <path d="M100 250 L85 272 M160 245 L180 260 M180 290 L165 312 M85 300 L105 315"/>
      <path d="M370 250 L355 272 M430 245 L450 260 M450 290 L435 312 M355 300 L375 315"/>
    </g>
  </svg>
</section>

<span class="sheet-label sheet-label--inner-2">Inner Option 02</span>
<section class="inner inner--gold" aria-label="Inner spread, gold pockets">
  <svg width="520" height="368" viewBox="0 0 520 368" aria-hidden="true">
    <defs>
      <linearGradient id="pocketGold" x1="0" y1="0" x2="1" y2="0">
        <stop offset="0" stop-color="var(--yellow-deep)"/>
        <stop offset=".5" stop-color="var(--yellow)"/>
        <stop offset="1" stop-color="var(--yellow-deep)"/>
      </linearGradient>
    </defs>
    <line x1="260" y1="0" x2="260" y2="368" stroke="#c9cbce"/>
    <polygon points="0,190 240,190 258,368 0,368" fill="url(#pocketGold)"/>
    <polygon points="280,190 520,190 520,368 262,368" fill="url(#pocketGold)"/>
    <g stroke="#4a3a10" stroke-width="1.2">
      <path d="M100 250 L85 272 M160 245 L180 260 M180 290 L165 312 M85 300 L105 315"/>
      <path d="M370 250 L355 272 M430 245 L450 260 M450 290 L435 312 M355 300 L375 315"/>
    </g>
  </svg>
</section>

</body>
</html>
```